Bright Arch Group business card

Bright Arch Group is the parent company of Bright Arch Building, Bright Arch Plumbing and Bright Arch Renovating. We require a sophisticated business card that covers all aspects of the building and plumbing space without using told or construction items.

Industry/Entity Type

Construction Company

Contact Information for Business Card

Gareth Pimley
Director
0472915083
gareth@brightarch.com.au
Www.brightarch.com.au

Font styles to use
Serif
Sans Serif

Colors
3176b5
ffce3e
0692cd
34a7d8
fbee3e
faa54b

Requirements
Must have
• Logo on front
• Logo and details on rear.
Nice to have
• Maybe water mark or shadow effect with logo
Should not have
• Tools or any construction associated items

```html
<!DOCTYPE html>
<html lang="en">
<head>
<meta charset="utf-8">
<title>Bright Arch Group business card</title>
<link rel="stylesheet" href="https://fonts.googleapis.com/css2?family=Jost:wght@300&family=Open+Sans:wght@400;600;700&display=swap">
<style>
  :root {
    --stage: #000000;
    --card: #333436;
    --card-edge: #2d2e30;
    --accent: #f7871f;
    --ink: #ffffff;
    --ink-soft: #e6e6e6;
  }
  * { margin: 0; padding: 0; box-sizing: border-box; }
  html, body {
    width: 1200px; height: 900px; overflow: hidden;
    background: var(--stage);
  }
  .stage { position: relative; width: 1200px; height: 900px; }
  .card {
    position: absolute; top: 271px; width: 457px; height: 281px;
    border-radius: 13px;
    background: radial-gradient(ellipse at 50% 40%, var(--card) 0%, var(--card-edge) 100%);
    font-family: "Open Sans", Arial, sans-serif;
    color: var(--ink);
  }
  .card--front { left: 137px; }
  .card--back { left: 626px; }

  .brand { position: absolute; text-align: center; font-family: "Jost", "Century Gothic", sans-serif; font-weight: 300; color: var(--ink); text-transform: uppercase; }
  .brand__mark { display: block; margin: 0 auto 12px; width: 26px; height: 26px; border-radius: 50%; background: var(--accent); }
  .brand__line { display: block; line-height: 1; }
  .card--front .brand { left: 296px; top: 42px; transform: translateX(-50%); white-space: nowrap; }
  .card--front .brand__main { font-size: 28px; letter-spacing: 0.2em; }
  .card--front .brand__sub { font-size: 19px; letter-spacing: 0.55em; margin-top: 6px; padding-left: 0.55em; }
  .card--back .brand { left: 186px; top: 50px; transform: translateX(-50%); white-space: nowrap; }
  .card--back .brand__main { font-size: 32px; letter-spacing: 0.2em; }
  .card--back .brand__sub { font-size: 22px; letter-spacing: 0.55em; margin-top: 6px; padding-left: 0.55em; }

  .person { position: absolute; left: 32px; top: 142px; }
  .person__name { font-size: 15.5px; font-weight: 700; color: var(--accent); line-height: 1.2; }
  .person__role { font-size: 11.5px; color: var(--ink-soft); line-height: 1.3; }

  .contact { position: absolute; left: 32px; top: 197px; list-style: none; }
  .contact__item { display: flex; align-items: center; gap: 7px; height: 16.5px; font-size: 12px; color: var(--ink-soft); }
  .contact__icon { width: 9px; height: 9px; fill: var(--accent); flex: none; }

  .divisions { position: absolute; left: 38px; top: 175px; list-style: none; }
  .divisions__item { display: flex; align-items: center; gap: 6px; height: 24px; font-size: 13.5px; font-weight: 600; }
  .divisions__item::before { content: ""; width: 6px; height: 6px; border-radius: 50%; background: var(--accent); }
</style>
</head>
<body>
<main class="stage">
  <section class="card card--front" aria-label="Card front">
    <div class="brand">
      <span class="brand__mark"></span>
      <span class="brand__line brand__main">Bright Arch</span>
      <span class="brand__line brand__sub">Group</span>
    </div>
    <div class="person">
      <p class="person__name">Gareth Pimley</p>
      <p class="person__role">Director</p>
    </div>
    <ul class="contact">
      <li class="contact__item">
        <svg class="contact__icon" viewBox="0 0 10 10"><path d="M2 0.5 L3.6 2.6 L2.8 3.6 Q3.8 5.8 6.4 7.2 L7.4 6.4 L9.5 8 L8.4 9.5 Q4.5 9.4 1.8 6.6 Q0.2 4.4 0.5 1.6 Z"/></svg>
        <span>0472915083</span>
      </li>
      <li class="contact__item">
        <svg class="contact__icon" viewBox="0 0 10 10"><path d="M0.5 2 H9.5 V8.5 H0.5 Z M0.5 2 L5 5.4 L9.5 2" stroke="#333436" stroke-width="0.8"/></svg>
        <span>gareth@brightarch.com.au</span>
      </li>
      <li class="contact__item">
        <svg class="contact__icon" viewBox="0 0 10 10"><circle cx="5" cy="5" r="4.6"/><path d="M2.5 3 Q4 4 3.5 6 M6 2 Q7.5 4.5 6.5 7.5" stroke="#333436" stroke-width="0.9" fill="none"/></svg>
        <span>Www.brightarch.com.au</span>
      </li>
    </ul>
  </section>

  <section class="card card--back" aria-label="Card back">
    <div class="brand">
      <span class="brand__line brand__main">Bright Arch</span>
      <span class="brand__line brand__sub">Group</span>
    </div>
    <ul class="divisions">
      <li class="divisions__item">Bright Arch Building</li>
      <li class="divisions__item">Bright Arch Plumbing</li>
      <li class="divisions__item">Bright Arch Renovating</li>
    </ul>
  </section>
</main>
</body>
</html>
```